50 years of Beno (birthday party)

I need a flyer that I can send to all guests as ChatterLoop.
Also as a digital file (e.g. PDF). Thanks!
Occasion: Beno's 50th birthday
It's a birthday party for family and friends
Location: Marquee at the sports ground, 4720 Hollerbach
Live music
Bar pub
Corrowby
Date: Saturday, May 25, 2024
Time: from 2 p.m. until open-end
Flexible participation - come and go as you please
Registration or deregistration: ChatterLoop on 076 - 312 58 27

Please create a flyer as an invitation. I want an Irish rock style with a touch of “Schlager” :-). There should be a real party.
Attention: no heavy metal style!!
It would be cool if a rock guitar and/or microphone were included.
Otherwise, I'm free and happy to be surprised. The flyer should not be too childish or youthful. There are practically no children at the event.

Additionally, please send a simpler flyer than “Save the date”.
Just the date and occasion.
Without place, time and registration.
With the note: Update follows...
The design is the same as the flyer with registration.
Updates

It would be cool if the Corrowby logo was visible too.
A whiskey glass would also be possible.
Balloons are not absolutely necessary - it looks like a children's party.
Please make the flyers rocky.

Target Market(s)

Family & Friends

Industry/Entity Type

look

Font styles to use
Other font styles liked:
• rockig

Colors

Designer to choose colors to be used in the design.

Requirements
Must have
• Irish rock design
Nice to have
• Rock guitar would be cool
Should not have
• comics

```html
<!DOCTYPE html>
<html lang="en">
<head>
<meta charset="utf-8">
<title>Beno's 50th Birthday – Flyer</title>
<link rel="stylesheet" href="https://fonts.googleapis.com/css2?family=Oswald:wght@500;600;700&family=Playball&display=swap">
<style>
  :root {
    --page-bg: #c8c8c8;
    --flyer-bg: #050404;
    --gold: #d9a83c;
    --gold-light: #f3d37a;
    --gold-dark: #9a6b1e;
    --white: #ffffff;
    --red: #e2262c;
  }
  * { margin: 0; padding: 0; box-sizing: border-box; }
  html, body {
    width: 980px; height: 1200px; overflow: hidden;
    background: var(--page-bg);
  }
  .flyer {
    position: absolute; left: 162px; top: 136px;
    width: 822px; height: 1162px;
    transform: scale(0.8); transform-origin: 0 0;
    background: var(--flyer-bg);
    overflow: hidden;
    font-family: 'Oswald', sans-serif;
  }
  .backdrop { position: absolute; inset: 0; }
  .sparkle-glow {
    position: absolute; left: 0; top: 0; width: 822px; height: 130px;
    background:
      radial-gradient(circle at 12% 30%, rgba(243,190,80,.45), transparent 18%),
      radial-gradient(circle at 88% 25%, rgba(243,190,80,.5), transparent 20%),
      radial-gradient(circle at 50% 10%, rgba(243,190,80,.25), transparent 30%);
  }
  .title {
    position: absolute; left: 0; width: 100%; top: 66px;
    text-align: center;
    font-weight: 700; font-size: 88px; line-height: 1;
    transform: scaleX(0.84);
    background: linear-gradient(180deg, var(--gold-light), var(--gold) 55%, var(--gold-dark));
    -webkit-background-clip: text; background-clip: text;
    -webkit-text-fill-color: transparent;
    white-space: nowrap;
  }
  .title sup { font-size: 40px; vertical-align: 36px; }
  .subtitle {
    position: absolute; left: 0; width: 100%; top: 166px;
    text-align: center; color: var(--white);
    font-family: 'Playball', cursive; font-size: 41px;
  }
  .date-block {
    position: absolute; left: 0; width: 100%; top: 368px;
    text-align: center;
  }
  .date-day { font-family: 'Playball', cursive; font-size: 48px; line-height: 1; color: var(--gold); }
  .date-main {
    font-weight: 600; font-size: 72px; line-height: 1.08; margin-top: 14px;
    color: var(--gold-light);
  }
  .illustration { position: absolute; border-radius: 40px; }
  .guitar-left {
    left: 150px; top: 350px; width: 112px; height: 300px;
    background: linear-gradient(160deg, #3a2a1a 0 35%, #e8961c 60%, #b86a10);
    transform: rotate(-12deg);
  }
  .guitar-right {
    left: 555px; top: 415px; width: 112px; height: 320px;
    background: linear-gradient(200deg, #c9a878 0 35%, #7a3a10 60%, #1a0a05);
    transform: rotate(22deg);
  }
  .microphone {
    left: 378px; top: 608px; width: 64px; height: 164px;
    background: linear-gradient(180deg, #e0c070, #8a6a28 55%, #1a1a1a 75%, #b8902e);
    border-radius: 30px 30px 12px 12px;
  }
  .highlights {
    position: absolute; left: 0; width: 100%; top: 800px;
    text-align: center; color: var(--white);
    font-family: 'Playball', cursive; font-size: 46px; line-height: 1.2;
  }
  .highlights .dot { color: var(--gold); font-size: 30px; vertical-align: 5px; }
  .participation {
    position: absolute; left: 0; width: 100%; top: 866px;
    text-align: center; color: var(--white);
    font-weight: 500; font-size: 24px; font-variant: small-caps; letter-spacing: 1px;
  }
  .time {
    position: absolute; left: 0; width: 100%; top: 906px;
    text-align: center; color: var(--gold);
    font-weight: 600; font-size: 37px; font-variant: small-caps; letter-spacing: 1.5px;
  }
  .location {
    position: absolute; left: 150px; top: 977px; width: 521px; height: 41px;
    border: 1.5px solid var(--gold); border-radius: 21px;
    display: flex; align-items: center; justify-content: center;
    font-weight: 500; font-size: 24px; font-variant: small-caps; letter-spacing: .5px;
    white-space: nowrap;
  }
  .location .label { color: var(--gold); margin-right: 6px; }
  .location .place { color: var(--red); }
  .registration {
    position: absolute; left: 0; width: 100%; top: 1030px;
    text-align: center; color: var(--white);
    font-family: 'Playball', cursive; font-size: 31px; line-height: 1.2;
  }
  .contact {
    position: absolute; left: 0; width: 100%; top: 1066px;
    text-align: center; color: var(--gold);
    font-weight: 500; font-size: 28px; font-variant: small-caps;
  }
</style>
</head>
<body>
<main class="flyer">
  <svg class="backdrop" width="822" height="1162" viewBox="0 0 822 1162" aria-hidden="true">
    <defs>
      <linearGradient id="wing" x1="0" y1="0" x2="0" y2="1">
        <stop offset="0" stop-color="#7a2433"/>
        <stop offset=".6" stop-color="#4a1520"/>
        <stop offset="1" stop-color="#050404" stop-opacity="0"/>
      </linearGradient>
      <linearGradient id="goldLine" x1="0" y1="0" x2="1" y2="1">
        <stop offset="0" stop-color="#9a6b1e"/>
        <stop offset=".5" stop-color="#f3d37a"/>
        <stop offset="1" stop-color="#b8862c"/>
      </linearGradient>
      <linearGradient id="hexFill" x1="0" y1="0" x2="0" y2="1">
        <stop offset="0" stop-color="#3a3a3c"/>
        <stop offset=".4" stop-color="#1a1718"/>
        <stop offset="1" stop-color="#0b0909"/>
      </linearGradient>
      <linearGradient id="bottomBand" x1="0" y1="0" x2="0" y2="1">
        <stop offset="0" stop-color="#5a1a24"/>
        <stop offset="1" stop-color="#1a0608"/>
      </linearGradient>
    </defs>
    <polygon points="0,255 210,378 210,800 0,800" fill="url(#wing)"/>
    <polygon points="822,255 612,378 612,800 822,800" fill="url(#wing)"/>
    <line x1="0" y1="255" x2="210" y2="378" stroke="url(#goldLine)" stroke-width="4"/>
    <line x1="822" y1="255" x2="612" y2="378" stroke="url(#goldLine)" stroke-width="4"/>
    <polygon points="410,245 620,368 620,652 410,775 200,652 200,368" fill="none" stroke="url(#goldLine)" stroke-width="8"/>
    <polygon points="410,270 600,380 600,640 410,750 220,640 220,380" fill="url(#hexFill)" stroke="url(#goldLine)" stroke-width="4"/>
    <polygon points="0,1040 330,1162 0,1162" fill="url(#bottomBand)"/>
    <polygon points="822,1040 492,1162 822,1162" fill="url(#bottomBand)"/>
    <line x1="0" y1="1022" x2="358" y2="1162" stroke="url(#goldLine)" stroke-width="4"/>
    <line x1="822" y1="1018" x2="458" y2="1162" stroke="url(#goldLine)" stroke-width="4"/>
  </svg>

  <div class="sparkle-glow" role="img" aria-label="Golden bokeh sparkles across the top edge"></div>

  <h1 class="title">BENO'S 50<sup>TH</sup> BIRTHDAY</h1>
  <p class="subtitle">It's a birthday party for family and friends</p>

  <div class="date-block">
    <p class="date-day">Saturday</p>
    <p class="date-main">MAY 25,<br>2024</p>
  </div>

  <div class="illustration guitar-left" role="img" aria-label="Orange electric guitar"></div>
  <div class="illustration guitar-right" role="img" aria-label="Sunburst electric guitar"></div>
  <div class="illustration microphone" role="img" aria-label="Gold vintage stage microphone"></div>

  <p class="highlights">Live music <span class="dot">•</span> Bar pub <span class="dot">•</span> Corrowby</p>
  <p class="participation">Flexible participation - come and go as you please</p>
  <p class="time">From 2 p.m. until open-end</p>

  <div class="location">
    <span class="label">Location:</span>
    <span class="place">Marquee at the sports ground, 4720 Hollerbach</span>
  </div>

  <p class="registration">Registration or deregistration:</p>
  <p class="contact">ChatterLoop on 076 - 312 58 27</p>
</main>
</body>
</html>
```